Government Contracting business needs a website design.

Pemberton & Quill, LLC is a minority owned Service Disabled Veteran Owned Small Business (SDVOSB) that provides Strategic Planning, Public Health Emergency Response, and Data Management Solutions for Federal Civilian and Defense Agencies. We have over 20 years of experience helping health and defense agencies develop concept of operations, deploy assets and personnel in Hot Zones around the world, and deliver goods and services all of the globe.

We are a leader in the field of Data Management. We help our customers develop cloud migration and disaster recovery strategies. We are experts with database management, data replication, queries, consolidation, and records management.

We are looking for a very nice and simple website designs that states clearly what we do as a company and that is easy for our customers to follow. We would like to have some moving pictures that are base on our expertise. We want the website to be easy to use and have the scroll down features that keeps things all on the same page when clicking on the menu. I attached a document with what we need on the website. I will also attach our logo. We want it to look simple clean and very professional.

Target Market(s)

Government Contracting, Management Consulting, Health

Industry/Entity Type

Government

Coding

Coded - Design and coding required

Number of Pages Required

1 page

Font styles to use
Serif

Requirements
Must have
• Very nice picture slides that speaks to our capabilities in Disaster Response, Strategic Planning, and Database Management. Slick look and design. Make sure SDVOSB Logo is right at the beginning of website as our customers is looking for that certification. Very nice colors that blend well with our logo.
Nice to have
• Very nice and slick colors that blends well with logo.
Should not have
• Basic website design that are weary on the eye. No bright colors, just simple colors that looks good with logo.

```html
<!DOCTYPE html>
<html lang="en">
<head>
<meta charset="utf-8">
<title>Pemberton &amp; Quill, LLC</title>
<link href="https://fonts.googleapis.com/css2?family=Tinos:wght@400;700&family=Lato:wght@400;700&display=swap" rel="stylesheet">
<style>
:root{
  --navy:#17466a;
  --blue:#1d5378;
  --blue-deep:#123a58;
  --ink:#1d4f73;
  --text:#4a4a4a;
  --muted:#6d6d6d;
  --pale:#c7d5e0;
  --white:#ffffff;
  --serif:'Tinos', 'Times New Roman', serif;
  --sans:'Lato', Arial, sans-serif;
}
*{box-sizing:border-box;margin:0;padding:0}
html,body{width:1200px;height:3711px;overflow:hidden}
body{font-family:var(--sans);color:var(--text);background:var(--white);position:relative}
section,header,footer{position:absolute;left:0;width:1200px}
.brand{display:flex;align-items:center;gap:12px;color:var(--white);font-family:var(--serif);font-size:24px}
.brand-mark{width:30px;height:30px;border:2px solid var(--white)}
/* nav */
.site-header{top:0;height:136px;background:var(--navy)}
.site-header .brand{position:absolute;left:80px;top:48px}
.main-nav{position:absolute;right:78px;top:56px;display:flex;gap:22px;font-size:16px;color:var(--white)}
.main-nav a{color:var(--white);text-decoration:none}
.main-nav .active{border-bottom:2px solid var(--white);padding-bottom:12px}
/* hero */
.hero{top:136px;height:574px;overflow:hidden;background:#2b3640}
.hero-photo{position:absolute;inset:0;
  background:
    radial-gradient(ellipse 260px 340px at 860px 300px,rgba(30,40,52,.55),rgba(30,40,52,0) 70%),
    radial-gradient(ellipse 420px 300px at 1080px 180px,rgba(240,243,246,.55),rgba(240,243,246,0) 70%),
    linear-gradient(100deg,#222c35 0%,#3a4651 30%,#6f7c88 52%,#b3bcc4 70%,#dfe3e7 100%)}
.hero-shade{position:absolute;left:0;top:0;width:600px;height:574px;background:linear-gradient(90deg,rgba(18,26,34,.72),rgba(18,26,34,0))}
.hero h1{position:absolute;left:80px;top:108px;width:420px;font-family:var(--serif);font-size:25px;line-height:36px;color:var(--white);font-weight:700}
.btn{display:inline-block;background:var(--blue);color:var(--white);font-size:17px;text-transform:uppercase;text-decoration:none}
.hero .btn{position:absolute;left:78px;top:354px;width:166px;height:60px;line-height:60px;text-align:center;font-family:var(--serif)}
.hero-icons{position:absolute;left:440px;top:0}
/* headings */
.section-title{font-family:var(--serif);font-weight:700;font-size:34px;color:var(--ink);display:flex;align-items:center;gap:14px}
.section-title .sq{width:22px;height:22px;border:3px solid currentColor}
.centered{justify-content:center}
/* why */
.why{top:710px;height:532px}
.why .section-title{position:absolute;left:80px;top:62px}
.why-intro{position:absolute;left:80px;top:126px;width:580px;font-size:13.5px;line-height:22px;color:var(--muted)}
.why-list{position:absolute;left:80px;top:212px;width:600px;list-style:none}
.why-list li{display:flex;gap:16px;margin-bottom:28px;font-family:var(--serif);font-weight:700;font-size:15px;line-height:22px;color:#3a3a3a}
.why-list svg{flex:none;margin-top:2px}
.why-photo{position:absolute;left:716px;top:60px;width:380px;height:472px;
  background:
    radial-gradient(ellipse 150px 210px at 220px 250px,rgba(190,178,164,.55),rgba(190,178,164,0) 75%),
    linear-gradient(180deg,#f3f1ee 0%,#e4ddd5 40%,#d8d3cd 70%,#f7f7f7 100%)}
/* agencies */
.agencies{top:1242px;height:478px;background:linear-gradient(180deg,#2b3440 0%,#3e4954 50%,#2a333d 100%)}
.agencies .section-title{position:absolute;left:0;top:60px;width:1200px;color:var(--white)}
.agency-grid{position:absolute;left:77px;top:156px;display:flex;gap:26px}
.agency{width:188px;height:227px;background:var(--white);text-align:center;padding-top:22px}
.agency .seal{width:104px;height:104px;border-radius:50%;background:#2f4560;margin:0 auto}
.agency .seal.sq{border-radius:0;width:112px;height:80px;margin-top:12px;background:#8a9aad}
.agency p{margin-top:30px;font-size:16px;line-height:22px;color:var(--ink);padding:0 10px}
/* capabilities */
.capabilities{top:1720px;height:531px}
.capabilities .section-title{position:absolute;left:0;top:62px;width:1200px}
.cap-grid{position:absolute;left:77px;top:142px;display:flex;gap:27px}
.cap{width:240px;text-align:center}
.cap-tile{display:block;height:170px}
.cap h3{margin-top:26px;font-family:var(--sans);font-weight:400;font-size:18px;line-height:24px;color:var(--ink);height:56px;display:flex;align-items:center;justify-content:center}
.cap p{margin-top:14px;font-size:13.5px;line-height:23px;color:var(--muted);padding:0 10px}
/* team */
.team{top:2251px;height:292px;background:linear-gradient(90deg,#1c4f74 0%,#2a5f86 55%,#3a6d93 100%)}
.team h2{position:absolute;left:80px;top:52px;font-family:var(--serif);font-size:32px;color:var(--white)}
.team-copy{position:absolute;left:80px;top:110px;width:590px;font-size:13px;line-height:22px;color:#e5edf3}
.team-copy p+p{margin-top:10px}
.member{position:absolute;top:54px;width:240px;text-align:center;color:var(--white)}
.member .portrait{width:102px;height:102px;border-radius:50%;border:3px solid var(--white);margin:0 auto;background:linear-gradient(160deg,#c9b29c,#7d6a5a)}
.member h4{margin-top:14px;font-family:var(--serif);font-weight:400;font-size:16px;white-space:nowrap}
.member span{display:block;margin-top:4px;font-size:13px;font-weight:700;line-height:18px}
/* blog */
.blog{top:2543px;height:438px}
.blog .section-title{position:absolute;left:0;top:62px;width:1200px}
.post{position:absolute;top:146px;width:502px;height:218px;display:flex}
.post-photo{width:250px;height:218px;position:relative}
.post-date{position:absolute;right:0;top:0;width:64px;height:60px;background:var(--white);opacity:.9;text-align:center;color:var(--ink);font-size:13px;line-height:16px;padding-top:8px}
.post-date b{display:block;font-size:20px;line-height:22px}
.post-body{flex:1;background:var(--blue);color:var(--white);padding:14px 14px 0 16px}
.post-body h3{font-family:var(--sans);font-weight:400;font-size:20px;line-height:24px;width:200px}
.post-body p{margin-top:12px;font-size:12.5px;line-height:18px;color:#e3ebf2}
.read-more{margin-top:18px;display:flex;align-items:center;gap:14px;font-size:13px}
/* about */
.about{top:2981px;height:260px;background:var(--pale)}
.about h2{position:absolute;left:84px;top:60px;font-family:var(--serif);font-size:32px;color:var(--ink)}
.about p{position:absolute;left:80px;top:122px;width:830px;font-size:13px;line-height:22px;color:var(--text)}
.about .btn{position:absolute;left:955px;top:126px;width:166px;height:60px;line-height:60px;text-align:center}
/* footer */
.site-footer{top:3241px;height:396px;background:var(--blue-deep);color:var(--white)}
.site-footer .brand{position:absolute;left:80px;top:70px;font-size:22px}
.foot-about{position:absolute;left:80px;top:150px;width:250px;text-align:center;font-size:13.5px;line-height:22px}
.socials{position:absolute;left:166px;top:262px;display:flex;gap:8px}
.socials span{width:26px;height:26px;border:1.5px solid var(--white);border-radius:50%}
.foot-col{position:absolute;top:62px}
.foot-col h5{font-family:var(--serif);font-size:18px;margin-bottom:20px}
.foot-links{list-style:none;font-size:13.5px;line-height:29px}
.contact-row{display:flex;gap:16px;font-size:13.5px;line-height:22px;margin-bottom:18px}
.newsletter p{font-size:13.5px;line-height:22px;width:250px}
.email-field{margin-top:14px;width:250px;height:60px;background:var(--white);color:#777;font-size:13px;line-height:60px;padding-left:10px}
.submit{margin-top:10px;width:156px;height:52px;background:#000;color:var(--white);text-align:center;line-height:52px;font-size:16px;font-weight:700}
.copyright{position:absolute;left:0;top:3637px;width:1200px;height:74px;background:var(--blue-deep);border-top:1px solid #3b6283;color:var(--white);text-align:center;line-height:74px;font-size:13.5px}
</style>
</head>
<body>

<header class="site-header">
  <div class="brand"><span class="brand-mark"></span>Pemberton &amp; Quill, LLC</div>
  <nav class="main-nav">
    <a class="active" href="#home">Home</a><a href="#about">About</a><a href="#why">Why Choose Us?</a><a href="#capabilities">Core Capabilities</a><a href="#services">Services</a><a href="#team">Team</a><a href="#join">Join Us</a><a href="#contact">Contact</a>
  </nav>
</header>

<section class="hero" id="home">
  <div class="hero-photo" role="img" aria-label="Photo of a businessman in a suit in front of a team meeting in a bright office"></div>
  <div class="hero-shade"></div>
  <h1>We are a Service Disabled Veteran Owned Small Business (SDVOSB) specializing in Mission Oriented Health IT for the Defense and VA Community.</h1>
  <a class="btn" href="#about">Read More</a>
  <svg class="hero-icons" width="260" height="574" viewBox="0 0 260 574">
    <path d="M170 -10 Q 60 290 150 590" fill="none" stroke="#1d5378" stroke-width="14"/>
    <g fill="#fff" stroke="#1d5378" stroke-width="3">
      <circle cx="100" cy="100" r="40"/><circle cx="68" cy="214" r="40"/><circle cx="68" cy="311" r="33"/><circle cx="80" cy="400" r="33"/><circle cx="100" cy="482" r="26"/>
    </g>
    <g fill="#1b1b1b">
      <path d="M94 82h12v12h12v12h-12v12h-12v-12h-12v-12h12z"/>
      <rect x="54" y="214" width="6" height="14"/><rect x="64" y="204" width="6" height="24"/><rect x="74" y="198" width="6" height="30"/>
      <rect x="52" y="298" width="32" height="20" fill="none" stroke="#1b1b1b" stroke-width="3"/><rect x="46" y="320" width="44" height="4"/>
      <circle cx="80" cy="400" r="16" fill="none" stroke="#1b1b1b" stroke-width="3"/><path d="M64 400h32M80 384v32" stroke="#1b1b1b" stroke-width="2"/>
      <circle cx="100" cy="474" r="6"/><path d="M88 494a12 10 0 0 1 24 0z"/>
    </g>
  </svg>
</section>

<section class="why" id="why">
  <h2 class="section-title"><span class="sq"></span>Why Choose Us?</h2>
  <p class="why-intro">Pemberton &amp; Quill, LLC is a minority owned Service Disabled Veteran Owned Small Business (SDVOSB) that provides Strategic Planning, Public Health Emergency Response, and Data Management Solutions for Federal Civilian and Defense Agencies.</p>
  <ul class="why-list">
    <li><svg width="20" height="20" viewBox="0 0 20 20"><rect x="1" y="3" width="15" height="15" fill="none" stroke="#1d4f73" stroke-width="2"/><path d="M4 10l5 5 10-13" fill="none" stroke="#1d4f73" stroke-width="2.5"/></svg>Over 20 years of experience deploying assets and personnel to disaster zones around the US and the world.</li>
    <li><svg width="20" height="20" viewBox="0 0 20 20"><rect x="1" y="3" width="15" height="15" fill="none" stroke="#1d4f73" stroke-width="2"/><path d="M4 10l5 5 10-13" fill="none" stroke="#1d4f73" stroke-width="2.5"/></svg>Over 20 years of experience developing concept of operations and stakeholder management strategies for Federal Agencies.</li>
    <li><svg width="20" height="20" viewBox="0 0 20 20"><rect x="1" y="3" width="15" height="15" fill="none" stroke="#1d4f73" stroke-width="2"/><path d="M4 10l5 5 10-13" fill="none" stroke="#1d4f73" stroke-width="2.5"/></svg>Over 10 years of experience with database management and replications.</li>
    <li><svg width="20" height="20" viewBox="0 0 20 20"><rect x="1" y="3" width="15" height="15" fill="none" stroke="#1d4f73" stroke-width="2"/><path d="M4 10l5 5 10-13" fill="none" stroke="#1d4f73" stroke-width="2.5"/></svg>Highly educated consultants with over 90% possessing advance degrees and industry certifications</li>
  </ul>
  <div class="why-photo" role="img" aria-label="Photo of a smiling businesswoman in a light blazer pointing upward"></div>
</section>

<section class="agencies" aria-label="Agencies We Serve">
  <div style="position:absolute;inset:0" role="img" aria-label="Dim background photo of an office meeting"></div>
  <h2 class="section-title centered"><span class="sq"></span>Agencies We Serve</h2>
  <div class="agency-grid">
    <div class="agency"><div class="seal"></div><p>Land Defense Office</p></div>
    <div class="agency"><div class="seal"></div><p>Civil Flight Agency</p></div>
    <div class="agency"><div class="seal sq"></div><p>Center for Health Readiness</p></div>
    <div class="agency"><div class="seal"></div><p>Aerial Command Bureau</p></div>
    <div class="agency"><div class="seal sq"></div><p>Institute of Health Research</p></div>
  </div>
</section>

<section class="capabilities" id="capabilities">
  <h2 class="section-title centered"><span class="sq"></span>Core Capabilities</h2>
  <div class="cap-grid">
    <div class="cap">
      <svg class="cap-tile" width="240" height="170" viewBox="0 0 240 170"><polygon points="6,46 240,6 240,132 6,170" fill="#cfcfcf" opacity=".6"/><polygon points="0,40 234,0 234,126 0,164" fill="#ececec" stroke="#d4d4d4"/><g fill="none" stroke="#333" stroke-width="3"><rect x="103" y="52" width="28" height="20" rx="3"/><circle cx="117" cy="86" r="7"/><path d="M103 112v-8a14 10 0 0 1 28 0v8"/></g></svg>
      <h3>Strategic Planning</h3>
      <p>Lorem Ipsum is simply dummy text of the printing and texting typesetting industry.</p>
    </div>
    <div class="cap">
      <svg class="cap-tile" width="240" height="170" viewBox="0 0 240 170"><polygon points="6,46 240,6 240,132 6,170" fill="#cfcfcf" opacity=".6"/><polygon points="0,40 234,0 234,126 0,164" fill="#ececec" stroke="#d4d4d4"/><g fill="none" stroke="#333" stroke-width="3"><path d="M117 84 L101 68 a9 9 0 0 1 16 -10 a9 9 0 0 1 16 10z"/><path d="M101 72h8l4-6 6 12 4-6h8"/><path d="M93 100q24 10 48 -4"/></g></svg>
      <h3>Public Health<br>Emergency Response</h3>
      <p>Lorem Ipsum is simply dummy text of the printing and texting typesetting industry.</p>
    </div>
    <div class="cap">
      <svg class="cap-tile" width="240" height="170" viewBox="0 0 240 170"><polygon points="6,46 240,6 240,132 6,170" fill="#cfcfcf" opacity=".6"/><polygon points="0,40 234,0 234,126 0,164" fill="#ececec" stroke="#d4d4d4"/><g fill="none" stroke="#333" stroke-width="3"><ellipse cx="109" cy="52" rx="16" ry="6"/><path d="M93 52v42a16 6 0 0 0 32 0v-42M93 66a16 6 0 0 0 32 0M93 80a16 6 0 0 0 32 0"/><rect x="131" y="62" width="14" height="20"/></g></svg>
      <h3>Data Management<br>Services</h3>
      <p>Lorem Ipsum is simply dummy text of the printing and texting typesetting industry.</p>
    </div>
    <div class="cap">
      <svg class="cap-tile" width="240" height="170" viewBox="0 0 240 170"><polygon points="6,46 240,6 240,132 6,170" fill="#cfcfcf" opacity=".6"/><polygon points="0,40 234,0 234,126 0,164" fill="#ececec" stroke="#d4d4d4"/><g fill="none" stroke="#333" stroke-width="3"><path d="M101 48h24l10 10v46h-34z"/><path d="M107 64h18M107 74h18M107 84h10"/><circle cx="129" cy="98" r="9"/></g></svg>
      <h3>Contracts Vehicles</h3>
      <p>Lorem Ipsum is simply dummy text of the printing and texting typesetting industry.</p>
    </div>
  </div>
</section>

<section class="team" id="team">
  <h2>Our Technical Team</h2>
  <div class="team-copy">
    <p>Lorem Ipsum is simply dummy text of the printing and typesetting industry. Lorem Ipsum has been the industry's standard dummy text ever since the 1500s, when an unknown printer took a galley of type and scrambled imake a type specimen book.</p>
    <p>Lorem Ipsum is simply dummy text of the printing and typesetting industry. Lorem Ipsum has been the industry's standard dummy text ever since the 1500s.</p>
  </div>
  <div class="member" style="left:650px"><div class="portrait" role="img" aria-label="Portrait of the President and CEO"></div><h4>Ret. SFC Marcus T. Pemberton</h4><span>President &amp; CEO</span></div>
  <div class="member" style="left:898px"><div class="portrait" role="img" aria-label="Portrait of the Business Development Manager"></div><h4>Mr. Daniel K. Whitford</h4><span>Business Development<br>Manager</span></div>
</section>

<section class="blog">
  <h2 class="section-title centered"><span class="sq"></span>Recent Blog</h2>
  <article class="post" style="left:77px">
    <div class="post-photo" role="img" aria-label="Photo of two children sitting on grass" style="background:linear-gradient(160deg,#7a9a3e,#4f7a2a 60%,#a3b86a)"><div class="post-date"><b>06</b>April</div></div>
    <div class="post-body"><h3>Lorem Ipsum is simply dummy</h3><p>Lorem Ipsum is simply dummy text of the printing and typesetting industry. Lorem Ipsum</p><div class="read-more">READ MORE <svg width="28" height="10" viewBox="0 0 28 10"><path d="M0 5h26M21 1l5 4-5 4" fill="none" stroke="#fff" stroke-width="1.5"/></svg></div></div>
  </article>
  <article class="post" style="left:623px">
    <div class="post-photo" role="img" aria-label="Photo of a smiling couple looking at a phone outdoors" style="background:linear-gradient(160deg,#b9cbd8,#8b9aa5 50%,#5a8f8a)"><div class="post-date"><b>06</b>April</div></div>
    <div class="post-body"><h3>Lorem Ipsum is simply dummy</h3><p>Lorem Ipsum is simply dummy text of the printing and typesetting industry. Lorem Ipsum</p><div class="read-more">READ MORE <svg width="28" height="10" viewBox="0 0 28 10"><path d="M0 5h26M21 1l5 4-5 4" fill="none" stroke="#fff" stroke-width="1.5"/></svg></div></div>
  </article>
</section>

<section class="about" id="about">
  <h2>About Pemberton &amp; Quill, LLC</h2>
  <p>Lorem Ipsum is simply dummy text of the printing and typesetting industry. Lorem Ipsum has been the industry's standard dummy text ever since the 1500s, when an unknown printer took a galley of type and scrambled it to make a type specimen book. It has survived not only five centuries, but also the leap into electronic typesetting, remaining essentially unchanged. .</p>
  <a class="btn" href="#join">Join Us Now</a>
</section>

<footer class="site-footer" id="contact">
  <div class="brand"><span class="brand-mark"></span>Pemberton &amp; Quill, LLC</div>
  <p class="foot-about">Lorem Ipsum is simply dummy text of the printing and typesetting industry. Lorem Ipsum has been the industry's standard dummy text ever since the 1500s.</p>
  <div class="socials"><span></span><span></span><span></span></div>
  <div class="foot-col" style="left:408px">
    <h5>Useful Links</h5>
    <ul class="foot-links"><li>Home</li><li>About</li><li>Why Choose Us</li><li>Core Capabilities</li><li>Services</li><li>Team</li><li>Join Us</li><li>Contact</li></ul>
  </div>
  <div class="foot-col" style="left:596px">
    <h5>Get In Touch</h5>
    <div class="contact-row"><svg width="14" height="20" viewBox="0 0 14 20"><path d="M7 0a7 7 0 0 1 7 7c0 5-7 13-7 13S0 12 0 7a7 7 0 0 1 7-7z" fill="#fff"/><circle cx="7" cy="7" r="2.5" fill="#123a58"/></svg><span>1870 Larkspur Ridge Rd,<br>Columbus, OH</span></div>
    <div class="contact-row"><svg width="16" height="16" viewBox="0 0 16 16"><path d="M3 1l3 3-2 2c1 2 3 4 5 5l2-2 3 3-2 3C7 15 1 9 1 3z" fill="#fff"/></svg><span>614-555-0142</span></div>
    <div class="contact-row"><svg width="16" height="12" viewBox="0 0 16 12"><rect x="0.5" y="0.5" width="15" height="11" fill="none" stroke="#fff"/><path d="M0.5 0.5l7.5 6 7.5-6" fill="none" stroke="#fff"/></svg><span>info@pembertonquill.com</span></div>
  </div>
  <div class="foot-col newsletter" style="left:872px">
    <h5>Newsletter</h5>
    <p>Would you like to receive exclusive access to articles, white papers and our regular monthly newsletter?</p>
    <div class="email-field">Enter Email Id</div>
    <div class="submit">SUBMIT</div>
  </div>
</footer>
<div class="copyright">© 2018 by Pemberton &amp; Quill, LLC. All Right Reserved.</div>

</body>
</html>
```